Design WORDPRESS Website for E Commerce Business

We are needing a WORDPRESS website for an E Commerce Business that is supplying quailty kids / baby products.

Target Market(s)

Female / Working Mums / New Mums

Industry/Entity Type

Business

Number of Pages Required

1 page

Font styles to use
Sans Serif

Colors
33b8a4
f8fcfd
d3a5cc
f7f1f7
cbcbcb
9d9d9d

```html
<!DOCTYPE html>
<html lang="en">
<head>
<meta charset="utf-8">
<title>Little Sprout — Kids &amp; Baby Store</title>
<link rel="stylesheet" href="https://fonts.googleapis.com/css2?family=Open+Sans:wght@400;600&family=Bebas+Neue&family=Raleway:wght@400;500&display=swap">
<style>
:root{
  --teal:#33b8a4;
  --ice:#f8fcfd;
  --pink:#d3a5cc;
  --blush:#f7f1f7;
  --line:#cbcbcb;
  --grey:#9d9d9d;
  --ink:#222;
  --nav:#0e0e0e;
  --text:#555;
}
*{margin:0;padding:0;box-sizing:border-box}
html,body{width:1200px;height:1200px;overflow:hidden;background:#fff}
body{position:relative;font-family:"Open Sans",sans-serif;color:var(--text)}
.abs{position:absolute}

/* top bar */
.topbar{left:0;top:0;width:1200px;height:37px;border-bottom:1px solid #e4e4e4}
.contact{left:150px;top:11px;font-size:11px;color:#666;display:flex;gap:18px;align-items:center}
.contact span{display:flex;align-items:center;gap:6px}
.top-icons{right:150px;top:9px;display:flex;gap:8px;align-items:center}
.top-icons .dot{width:20px;height:20px;border-radius:50%}

/* header */
.brand{left:152px;top:54px;display:flex;align-items:center;gap:8px}
.brand-mark{width:24px;height:24px;border-radius:50%;background:var(--grey)}
.brand-name{font-family:"Open Sans",sans-serif;font-weight:400;font-size:20px;line-height:24px;color:var(--teal);letter-spacing:.5px;white-space:nowrap}
.search{left:552px;top:50px;width:392px;height:33px;border:1px solid var(--line);display:flex;align-items:center}
.search .cat{font-size:12px;color:#444;padding:0 12px 0 9px;border-right:1px solid #bbb;line-height:12px;display:flex;gap:8px;align-items:center}
.search .ph{font-size:10px;color:#888;padding-left:14px;flex:1}
.search .go{width:36px;height:33px;background:#333;display:flex;align-items:center;justify-content:center;margin-right:-1px}
.cart{left:959px;top:50px;width:92px;height:33px;border:1px solid var(--line);border-radius:3px;display:flex;align-items:center;gap:8px;padding-left:10px;font-size:12px;color:#444}

/* hero */
.hero{left:0;top:98px;width:1200px;height:487px;background:linear-gradient(100deg,#5d5e63 0%,#807872 30%,#8e8780 55%,#c9c6c8 80%,#b9b5b7 100%)}
.hero-shade{left:0;top:98px;width:1200px;height:487px;background:rgba(0,0,0,.35)}
.nav{left:150px;top:98px;width:900px;height:76px;display:flex}
.nav a{flex:1;background:var(--nav);color:#fff;text-decoration:none;font-size:12px;display:flex;flex-direction:column;align-items:center;justify-content:center;gap:8px;border-right:1px solid #333}
.nav a:last-child{border-right:0}
.nav a.active{background:var(--teal)}
.hero-title{left:600px;top:279px;font-family:"Open Sans",sans-serif;font-weight:400;font-size:38px;color:#fff;letter-spacing:1px;white-space:nowrap}
.hero-copy{left:603px;top:330px;width:470px;font-size:16px;line-height:27px;color:#fff}
.hero-btn{left:603px;top:392px;width:165px;height:41px;background:var(--teal);color:#fff;font-size:16px;display:flex;align-items:center;justify-content:center;gap:14px}
.dots{left:584px;top:555px;display:flex;gap:4px}
.dots i{width:9px;height:9px;border:1px solid #fff;border-radius:50%}
.dots i.on{background:#fff}

/* category tiles */
.tile{overflow:hidden}
.tile-boys{left:150px;top:615px;width:450px;height:315px;background:linear-gradient(90deg,#3a3a3a,#2b2b2b 60%,#1f1f1f)}
.tile-girls{left:602px;top:615px;width:448px;height:156px;background:linear-gradient(90deg,#555 0%,#5a5a5a 60%,#6b6663 100%)}
.tile-babys{left:602px;top:773px;width:448px;height:157px;background:linear-gradient(90deg,#5a5858,#6e6562 60%,#7d6f69)}
.t-shop,.t-big{position:absolute;text-align:center;color:#fff;font-family:"Bebas Neue",sans-serif;line-height:1;white-space:nowrap}
.t-for{position:absolute;background:var(--pink);color:#fff;font-family:"Open Sans",sans-serif;display:flex;align-items:center;justify-content:center}
.rule{position:absolute;height:1px;background:#ddd}

/* products */
.kicker{left:0;width:1200px;top:971px;text-align:center;font-family:"Raleway",sans-serif;font-size:13px;color:var(--pink);letter-spacing:.5px}
.heading{left:0;width:1200px;top:989px;text-align:center;font-family:"Raleway",sans-serif;font-weight:500;font-size:27px;color:var(--ink);letter-spacing:2px}
.heading-rule{left:525px;top:1029px;width:150px;height:3px;background:#777}
.tabs{left:431px;top:1057px;display:flex;align-items:center}
.tabs span{width:76px;height:28px;border:1px solid #999;font-family:"Raleway",sans-serif;font-size:11px;color:#444;display:flex;align-items:center;justify-content:center}
.tabs b{width:11px;height:1px;background:#999}
.tabs span.on{background:var(--pink);border-color:var(--pink);color:#fff}
.card{top:1114px;width:208px;height:100px;border:1px solid #e6e6e6;border-bottom:0}
.card .ph{position:absolute;left:50%;transform:translateX(-50%);top:22px;width:90px;height:80px;border-radius:6px}
.badge{position:absolute;left:1px;top:16px;height:26px;padding:0 7px;font-size:12px;color:#fff;display:flex;align-items:center;letter-spacing:1px}
</style>
</head>
<body>

<div class="abs topbar"></div>
<div class="abs contact">
  <span><svg width="13" height="10" viewBox="0 0 13 10" fill="none" stroke="#888"><rect x=".5" y=".5" width="12" height="9"/><path d="M.5 .5l6 5 6-5"/></svg>hello@littlesprout.com</span>
  <span><svg width="12" height="12" viewBox="0 0 24 24" fill="none" stroke="#888" stroke-width="2"><path d="M22 16.9v3a2 2 0 0 1-2.2 2 19.8 19.8 0 0 1-8.6-3.1 19.5 19.5 0 0 1-6-6A19.8 19.8 0 0 1 2.1 4.2 2 2 0 0 1 4.1 2h3a2 2 0 0 1 2 1.7c.1 1 .4 1.9.7 2.8a2 2 0 0 1-.5 2.1L8 9.9a16 16 0 0 0 6 6l1.3-1.3a2 2 0 0 1 2.1-.4c.9.3 1.8.6 2.8.7a2 2 0 0 1 1.7 2z"/></svg>+91 555.010.2040</span>
</div>
<div class="abs top-icons">
  <svg width="15" height="15" viewBox="0 0 16 16" fill="none" stroke="#777" stroke-width="1.3"><circle cx="8" cy="8" r="7"/><circle cx="8" cy="6.5" r="2.5"/><path d="M3.5 13c1-2 2.6-3 4.5-3s3.5 1 4.5 3"/></svg>
  <svg width="15" height="14" viewBox="0 0 16 14" fill="none" stroke="#777" stroke-width="1.3"><path d="M8 13S1 8.5 1 4.5A3.5 3.5 0 0 1 8 3a3.5 3.5 0 0 1 7 1.5C15 8.5 8 13 8 13z"/></svg>
  <svg width="14" height="14" viewBox="0 0 14 14" fill="none" stroke="#777" stroke-width="1.2"><rect x="2" y="1" width="10" height="12"/><path d="M4 4h6M4 7h6M4 10h4"/></svg>
  <span style="width:6px"></span>
  <i class="dot" style="background:#55acee"></i>
  <i class="dot" style="background:#3b5998"></i>
  <i class="dot" style="background:#dd4b39"></i>
  <i class="dot" style="background:#0e76a8"></i>
</div>

<div class="abs brand">
  <i class="brand-mark"></i>
  <div class="brand-name">LITTLE SPROUT</div>
</div>
<div class="abs search">
  <div class="cat">All Categories <svg width="7" height="4"><path d="M0 0h7L3.5 4z" fill="#333"/></svg></div>
  <div class="ph">Search entire store here...</div>
  <div class="go"><svg width="14" height="14" viewBox="0 0 14 14" fill="none" stroke="#fff" stroke-width="2"><circle cx="6" cy="6" r="4.5"/><path d="M9.5 9.5l3.5 3.5"/></svg></div>
</div>
<div class="abs cart">
  <svg width="20" height="16" viewBox="0 0 20 16" fill="none" stroke="#555" stroke-width="1.3"><path d="M1 5h18l-2 10H3z"/><path d="M6 5l3-4M14 5l-3-4"/><circle cx="15" cy="3" r="3" fill="var(--teal)" stroke="none"/></svg>
  $00.00
</div>

<div class="abs hero" role="img" aria-label="Photo of a toddler playing with a soft toy ball in a bright nursery"></div>
<div class="abs hero-shade"></div>

<nav class="abs nav">
  <a class="active" href="#"><svg width="28" height="26" viewBox="0 0 28 26" fill="none" stroke="#fff" stroke-width="1.4"><path d="M2 13L14 2l12 11M5 10v15h18V10M11 25v-8h6v8"/></svg>HOME</a>
  <a href="#"><svg width="28" height="26" viewBox="0 0 28 26" fill="none" stroke="#fff" stroke-width="1.3"><rect x="1" y="1" width="7" height="6"/><rect x="10.5" y="1" width="7" height="6"/><rect x="20" y="1" width="7" height="6"/><rect x="1" y="10" width="7" height="6"/><rect x="10.5" y="10" width="7" height="6"/><rect x="20" y="10" width="7" height="6"/><rect x="1" y="19" width="7" height="6"/><rect x="10.5" y="19" width="7" height="6"/><rect x="20" y="19" width="7" height="6"/></svg>ALL</a>
  <a href="#"><svg width="24" height="26" viewBox="0 0 24 26" fill="none" stroke="#fff" stroke-width="1.3"><circle cx="7" cy="4" r="3"/><circle cx="17" cy="4" r="3"/><path d="M3 9h8v9H3zM13 9h8v9h-8zM5 18v7M9 18v7M15 18v7M19 18v7"/></svg>BOYS</a>
  <a href="#"><svg width="24" height="26" viewBox="0 0 24 26" fill="none" stroke="#fff" stroke-width="1.3"><circle cx="7" cy="4" r="3"/><circle cx="17" cy="4" r="3"/><path d="M5 9h4l3 9H2zM15 9h4l3 9H12zM5 18v7M9 18v7M15 18v7M19 18v7"/></svg>GIRLS</a>
  <a href="#"><svg width="26" height="26" viewBox="0 0 26 26" fill="none" stroke="#fff" stroke-width="1.3"><circle cx="13" cy="14" r="10"/><circle cx="13" cy="4" r="2.5"/></svg>BABY</a>
  <a href="#"><svg width="40" height="26" viewBox="0 0 40 26" fill="none" stroke="#fff" stroke-width="1.3"><rect x="1" y="1" width="38" height="24"/><path d="M4 5h32M8 14h26" stroke-dasharray="2 2"/><circle cx="11" cy="10" r="3"/></svg>GIFT CARDS</a>
  <a href="#"><svg width="36" height="26" viewBox="0 0 36 26" fill="none" stroke="#fff" stroke-width="1.3"><path d="M20 3h9v9L14 25 6 17z"/><circle cx="25" cy="7" r="1.5"/><path d="M25 7c4-6 9-4 8 0"/></svg>SALE</a>
</nav>

<h1 class="abs hero-title">LOREM IPSUM IS SIMPLY</h1>
<p class="abs hero-copy">Lorem Ipsum is simply dummy text of the printing and typesetting industry. Lorem Ipsum has been the industry's</p>
<div class="abs hero-btn">Order Us <span>&gt;</span></div>
<div class="abs dots"><i></i><i class="on"></i><i></i></div>

<div class="abs tile tile-boys" role="img" aria-label="Photo of two young boys in caps and glasses">
  <div class="rule" style="left:212px;top:169px;width:196px"></div>
  <div class="t-shop" style="left:214px;width:200px;top:95px;font-size:56px">SHOP</div>
  <div class="t-for" style="left:272px;top:153px;width:70px;height:29px;font-size:18px">FOR</div>
  <div class="t-big" style="left:200px;width:220px;top:183px;font-size:76px">BOYS</div>
</div>
<div class="abs tile tile-girls" role="img" aria-label="Photo of a smiling little girl with butterflies">
  <div class="rule" style="left:23px;top:74px;width:165px"></div>
  <div class="t-shop" style="left:36px;width:140px;top:10px;font-size:49px">SHOP</div>
  <div class="t-for" style="left:76px;top:62px;width:59px;height:22px;font-size:15px">FOR</div>
  <div class="t-big" style="left:16px;width:180px;top:84px;font-size:67px">GIRLS</div>
</div>
<div class="abs tile tile-babys" role="img" aria-label="Photo of a laughing baby holding a toy">
  <div class="rule" style="left:23px;top:69px;width:165px"></div>
  <div class="t-shop" style="left:36px;width:140px;top:6px;font-size:49px">SHOP</div>
  <div class="t-for" style="left:76px;top:57px;width:59px;height:22px;font-size:15px">FOR</div>
  <div class="t-big" style="left:16px;width:180px;top:80px;font-size:67px">BABYS</div>
</div>

<div class="abs kicker">BEST SELLING PRODUCTS</div>
<h2 class="abs heading">OUR PRODUCTS</h2>
<div class="abs heading-rule"></div>
<div class="abs tabs"><span>ALL</span><b></b><span>BOYS</span><b></b><span>GIRLS</span><b></b><span class="on">BABY</span></div>

<div class="abs card" style="left:150px"><div class="ph" role="img" aria-label="Product photo of a baby bib on a hanger" style="background:linear-gradient(#e8eef5,#a9cde0)"></div><span class="badge" style="background:var(--pink)">20% OFF</span></div>
<div class="abs card" style="left:382px"><div class="ph" role="img" aria-label="Product photo of baby bath and skincare bottles" style="background:linear-gradient(#f6efe6,#e9c9d0)"></div></div>
<div class="abs card" style="left:612px"><div class="ph" role="img" aria-label="Product photo of a stack of printed baby bibs" style="background:linear-gradient(#f3ead8,#e6c48e)"></div><span class="badge" style="background:var(--teal)">New</span></div>
<div class="abs card" style="left:842px"><div class="ph" role="img" aria-label="Product photo of a bottle steriliser with baby bottles" style="background:linear-gradient(#f1eef5,#cdb6dc)"></div></div>

</body>
</html>
```